Premium wine label refresh for Birch &Vale wines

Our Birch & Vale label is dated. We're looking for a contemporary refresh that will stand out on the shelf, make a strong quality statement and a more contemporary look. Feel free to take a completely fresh approach but the label should connect with the brand story. Birch & Vale refers to my convict ancestry and is a tribute to humble beginnings. Where we finish is not necessarily where we start.

Target Market(s)

Aspirational, educated wine drinkers 30-55

Industry/Entity Type

Wine

Font styles to use
Sans Serif

Requirements
Must have
• Shelf presence, premium feel, connection to the existing label
Nice to have
• Print quality cues like embossing, foil etc.
Should not have
• Fun look and feel.

```html
<!DOCTYPE html>
<html lang="en">
<head>
<meta charset="utf-8">
<title>Birch &amp; Vale — Sauvignon Blanc 2022</title>
<link rel="stylesheet" href="https://fonts.googleapis.com/css2?family=Cinzel:wght@600;700&family=Roboto:wght@700&display=swap">
<style>
  :root {
    --label-black: #000000;
    --crest-panel: #070707;
    --silver: #dcdcdc;
    --crest-line: #8c8c8c;
    --ornament-core: #262626;
    --ornament-mid: #141414;
    --varietal-grey: #3c3c3c;
    --vintage-grey: #4a4a4a;
  }
  html, body {
    margin: 0;
    padding: 0;
    overflow: hidden;
    background: var(--label-black);
  }
  .label {
    position: relative;
    width: 1165px;
    height: 1200px;
    background: var(--label-black);
    overflow: hidden;
  }
  .crest-panel {
    position: absolute;
    left: 457px;
    top: 0;
    width: 314px;
    height: 304px;
    background: var(--crest-panel);
  }
  .crest {
    position: absolute;
    left: 503px;
    top: 36px;
    width: 222px;
    height: 222px;
    display: flex;
    flex-direction: column;
    align-items: center;
    justify-content: center;
    gap: 14px;
  }
  .crest-ring {
    width: 64px;
    height: 64px;
    border: 2px solid var(--crest-line);
    border-radius: 50%;
  }
  .crest-name {
    font-family: "Cinzel", serif;
    font-weight: 600;
    font-size: 20px;
    letter-spacing: 2px;
    color: var(--crest-line);
  }
  .ornament-field {
    position: absolute;
    left: 268px;
    top: 310px;
    width: 682px;
    height: 670px;
    border-radius: 50%;
    background: radial-gradient(circle at 50% 50%, var(--ornament-core) 0%, var(--ornament-mid) 50%, rgba(0,0,0,0) 71%);
  }
  .wordmark {
    position: absolute;
    left: 281px;
    top: 405px;
    width: 653px;
    height: 473px;
    margin: 0;
    display: flex;
    flex-direction: column;
    justify-content: center;
    font-family: "Cinzel", serif;
    font-weight: 700;
    font-size: 150px;
    line-height: 1.35;
    color: var(--silver);
    white-space: nowrap;
  }
  .wordmark-first { align-self: flex-start; }
  .wordmark-second { align-self: flex-end; }
  .varietal {
    position: absolute;
    left: 0;
    width: 100%;
    top: 1016px;
    margin: 0;
    text-align: center;
    font-family: "Cinzel", serif;
    font-weight: 700;
    font-size: 36px;
    letter-spacing: 1px;
    color: var(--varietal-grey);
  }
  .vintage {
    position: absolute;
    left: 0;
    width: 100%;
    top: 1072px;
    margin: 0;
    text-align: center;
    font-family: "Roboto", sans-serif;
    font-weight: 700;
    font-size: 24px;
    letter-spacing: 5px;
    color: var(--vintage-grey);
  }
</style>
</head>
<body>
  <main class="label">
    <div class="crest-panel"></div>
    <div class="crest">
      <span class="crest-ring"></span>
      <span class="crest-name">Birch &amp; Vale</span>
    </div>
    <div class="ornament-field" role="img" aria-label="Faint filigree rosette ornament behind the name"></div>
    <h1 class="wordmark"><span class="wordmark-first">Birch</span><span class="wordmark-second">&amp; Vale</span></h1>
    <p class="varietal">SAUVIGNON BLANC</p>
    <p class="vintage">2022</p>
  </main>
</body>
</html>
```